Car Club Website- RT Falcon Club of New Zealand

We have been running a website in NZ for RT Falcon Car enthusiasts. The design was fairly basic and is in serious need of a revamp, http://pelvatrunk.examplehost.org/index.html. We are looking for a dynamic design that will be visually attractive ( and obvious ) to our visitors and incorporates the fundamentals of the previous website. The inmportant tabs are the forum, gallery and events and the website needs to be easy to use for everyone.

This is all about the cars and the people. Visually, you need to recognise that we are a NZ Car Club and as such we do not want graphics of Left Hand Drive Cars or anything obviously NOT from NZ.
Thanks, cheers Rob

I AM VERY INTERESTED TO SEE SOMETHING THAT IS TOTALLY DIFFERENT TO ANYTHING YET POSTED. THE DESIGNS WE HAVE ARE GOOD AND I WILL PICK ONE OF THOSE BUT REALLY WANT TO SEE SOMETHING CREATIVE AND EYE CATCHING. I HAVE NOW CHANGED TO NON REFUNDABLE SO SOMEONE WILL GET PAID.
Updates

HI All, thanks for input so far but I have not seen a really creative left field approach yet which I am looking for. Thanks, cheers Rob

Target Market(s)

Car Enthusiasts

Industry/Entity Type

Events

Requirements
Must have
• as per link website
Should not have
• Any obvious graphics not from NZ

```html
<!DOCTYPE html>
<html lang="en">
<head>
<meta charset="utf-8">
<title>RT Falcon Club of New Zealand</title>
<link rel="stylesheet" href="https://fonts.googleapis.com/css2?family=Oswald:wght@400;500&family=Arimo:wght@400;700&display=swap">
<style>
:root{
  --red:#e4252b;
  --red-dark:#b8161c;
  --ink:#222;
  --text:#444;
  --muted:#666;
  --rule:#c9c9c9;
  --night:#0b0b0b;
  --panel:#f3f3f3;
}
*{box-sizing:border-box;margin:0;padding:0}
html,body{width:1200px;height:1092px;overflow:hidden}
body{position:relative;background:var(--night);font-family:"Arimo",Arial,sans-serif;color:var(--text)}
.abs{position:absolute}
.side-scene{top:0;height:1092px;width:214px;background:radial-gradient(ellipse at 70% 22%,#4a3a52 0%,#2a2a2e 22%,#121214 55%,#050505 100%)}
.side-scene.left{left:0}
.side-scene.right{right:0;background:radial-gradient(ellipse at 30% 22%,#4a3a52 0%,#2a2a2e 22%,#121214 55%,#050505 100%)}
.page{left:212px;top:0;width:778px;height:970px;background:#fff}
.newsbar{left:216px;top:0;width:768px;height:25px;background:#1c1c1c;color:#ddd;font-size:10px;line-height:25px;white-space:nowrap;overflow:hidden}
.newsbar .label{display:inline-block;background:#050505;color:#fff;font-weight:700;padding:0 14px 0 12px;margin-right:14px;position:relative}
.newsbar .label:after{content:"";position:absolute;right:-8px;top:0;border-left:8px solid #050505;border-top:12.5px solid transparent;border-bottom:12.5px solid transparent}
.masthead{left:216px;top:25px;width:768px;height:63px;background:linear-gradient(#3a3a3a,#161616 70%,#0e0e0e)}
.brand{left:24px;top:14px;display:flex;align-items:center;gap:8px;color:#fff;font-family:"Oswald",sans-serif;font-weight:500;font-size:21px;line-height:1;letter-spacing:.5px}
.brand .mark{width:12px;height:12px;background:var(--red)}
.brand small{display:block;font-size:11px;letter-spacing:2px;margin-top:3px}
.advert{right:20px;top:12px;text-align:right;color:#ddd;font-size:12px}
.advert .sponsor-name{display:block;margin-top:5px;font-size:20px;color:#cfcfcf}
.mainnav{left:216px;top:88px;width:768px;height:28px;background:var(--red);display:flex}
.mainnav a{font-family:"Oswald",sans-serif;font-size:13px;color:#fff;text-decoration:none;line-height:28px;padding:0 13px;text-transform:uppercase}
.mainnav a:first-child{padding-left:16px}
.mainnav a.active{background:#1b1b1b}
.search{position:absolute;right:33px;top:6px;width:150px;height:17px;background:#fff;border:0}
.search-icon{position:absolute;right:9px;top:6px}
.page-title{left:227px;top:123px;font-size:17px;font-weight:700;color:var(--ink)}
.slider{left:230px;top:149px;width:561px;height:188px;background:linear-gradient(#9a9aa2 0%,#6e6e78 45%,#4a4a50 70%,#2a2a2c 100%)}
.slider .arrow{position:absolute;top:80px}
.intro{left:235px;top:349px;width:558px}
.intro .lead{font-size:11.5px;line-height:19px;color:#111}
.intro .body{margin-top:5px;font-size:9.9px;line-height:15.8px;color:var(--text);text-align:justify}
.feature{top:485px;width:172px;height:262px}
.feature h2{font-size:13px;font-weight:700;color:var(--red-dark);white-space:nowrap}
.feature .photo{position:absolute;left:0;top:24px;width:172px;height:111px}
.feature p{position:absolute;left:0;top:146px;width:172px;font-size:9.6px;line-height:15.7px;text-align:justify}
.btn{display:inline-block;background:var(--red);color:#fff;font-size:12px;line-height:24px;padding:0 9px;border-radius:3px}
.feature .btn{position:absolute;left:0;top:236px}
.links{top:764px;width:120px}
.links h3{font-size:14px;font-weight:700;color:#333;margin-bottom:4px}
.links li{list-style:none;font-size:10px;line-height:19.5px;border-bottom:1px solid var(--rule);padding-left:1px;color:#333}
.links li:last-child{border-bottom:0}
.sidebar{left:802px;width:177px}
.box-head{height:28px;background:linear-gradient(#ee3a3f,#d61e24);color:#fff;font-family:"Oswald",sans-serif;font-size:12.5px;line-height:30px;padding-left:10px;text-transform:uppercase}
.events li{list-style:none;height:27px;background:linear-gradient(#e9e9e9,#cfcfcf);border-bottom:1px solid #f5f5f5;font-size:10px;line-height:27px;white-space:nowrap;overflow:hidden;color:#222}
.events b{display:inline-block;width:26px;text-align:center;font-family:"Oswald",sans-serif;font-weight:400;font-size:12px;color:#333}
.panel{border:1px solid #ddd;border-top:0;background:#fff}
.forum{height:382px;padding:1px 5px 4px 7px}
.forum .topic{padding-top:10px}
.forum h4{font-size:11.5px;line-height:13px;font-weight:400;color:#111;padding-left:1px}
.forum p{font-size:9.5px;line-height:12.5px;color:#555;padding-left:1px;margin-top:2px}
.forum .stats{display:flex;justify-content:space-between;font-size:9.5px;line-height:19px;border-top:1px solid #999;border-bottom:1px solid #ccc;margin-top:3px;padding:0 2px;color:#333}
.social{display:flex;gap:9px;padding:15px 20px 15px 21px}
.social span{width:27px;height:27px}
.newsletter{padding:13px 12px 0 11px;height:71px}
.newsletter .field{height:22px;border:1px solid #bbb;font-size:10px;line-height:20px;padding-left:6px;color:#333}
.newsletter .btn{float:right;margin-top:8px;font-size:12px;line-height:23px;padding:0 10px}
.footer{left:212px;top:970px;width:778px;height:28px;background:#2a2a2a;color:#aaa;font-size:10px;line-height:28px;padding-left:29px}
.sponsored{left:0;top:1008px;width:1200px;text-align:center;color:#fff;font-size:10px}
.sponsored .sponsor-name{display:block;margin-top:9px;font-size:15px;font-weight:700;color:#e08a2a}
</style>
</head>
<body>
<div class="abs side-scene left" role="img" aria-label="Dark studio photo of a purple sports car, left half"></div>
<div class="abs side-scene right" role="img" aria-label="Dark studio photo of a purple sports car, right half"></div>
<div class="abs page"></div>

<div class="abs newsbar"><span class="label">LATEST NEWS</span>Lorem Ipsum is simply dummy text of the printing and typesetting industry. Lorem Ipsum has been the industry's standard dummy text ever and play 1</div>

<header class="abs masthead">
  <div class="abs brand"><span class="mark"></span><div>RT FALCON CLUB<small>OF NEW ZEALAND</small></div></div>
  <div class="abs advert">Please support our advertisers who fund this site for the benefit of all<span class="sponsor-name">northshore motors</span></div>
</header>

<nav class="abs mainnav">
  <a href="#">Home</a><a href="#">Calendar</a><a href="#">Events</a><a href="#">Gallery</a><a href="#" class="active">Membership</a><a href="#">Forum</a><a href="#">Advertisers</a>
  <div class="search"></div>
  <svg class="search-icon" width="16" height="16" viewBox="0 0 16 16"><circle cx="6.5" cy="6.5" r="4.8" fill="none" stroke="#fff" stroke-width="2"/><line x1="10" y1="10" x2="14.5" y2="14.5" stroke="#fff" stroke-width="2.4" stroke-linecap="round"/></svg>
</nav>

<h1 class="abs page-title">Falcon's At home On the Track or On Show</h1>

<div class="abs slider" role="img" aria-label="Vintage twin-engine aircraft on an airfield with club cars parked beneath a cloudy sky">
  <svg class="arrow" style="left:12px" width="18" height="30" viewBox="0 0 18 30"><polyline points="15,2 3,15 15,28" fill="none" stroke="#fff" stroke-width="2.5"/></svg>
  <svg class="arrow" style="right:12px" width="18" height="30" viewBox="0 0 18 30"><polyline points="3,2 15,15 3,28" fill="none" stroke="#fff" stroke-width="2.5"/></svg>
</div>

<section class="abs intro">
  <p class="lead">This is not an official website related to the manufacture of RT Falcon cars but it is a website devoted to all those that share a passion for the RT Falcon.</p>
  <p class="body">Welcome to our website. Our aim is to make this site user friendly and we have included a 'Forum' for the benefit of all RT Falcon owners in New Zealand regardless of Falcon kit type. Our intent for the Forum is to give those people interested/active in the RT Falcon NZ scene a common vehicle to share ideas, problem solve and plan events. Our Calendar lists up-to-date and upcoming events. Check this regularly, especially for those last-minute runs that are often organised at very short notice upon the discovery of fine weather in Auckland!</p>
</section>

<article class="abs feature" style="left:235px">
  <h2>Riverside Concours 2010</h2>
  <div class="photo" role="img" aria-label="Dark blue roadster with gull-wing doors open on a black background" style="background:radial-gradient(ellipse at 50% 60%,#3c3c6a,#15152a 55%,#050508)"></div>
  <p>owners in New Zealand regardless of Falcon kit type. Our intent for the Forum is to give those people interested/active in the RT Falcon NZ scene a common vehicle to share ideas</p>
  <span class="btn">Read more</span>
</article>
<article class="abs feature" style="left:427px">
  <h2>Madness at Kereru Park</h2>
  <div class="photo" role="img" aria-label="View over a car bonnet along a country road following another roadster" style="background:linear-gradient(#b9c2c6,#8d979b 40%,#55605a 65%,#6f7a80)"></div>
  <p>owners in New Zealand regardless of Falcon kit type. Our intent for the Forum is to give those people interested/active in the RT Falcon NZ scene a common vehicle to share ideas</p>
  <span class="btn">Read more</span>
</article>
<article class="abs feature" style="left:615px">
  <h2>Falcon Club of New Zealand</h2>
  <div class="photo" role="img" aria-label="Yellow roadsters parked on grass under trees at a club meet" style="background:linear-gradient(#8a8f86,#4d4f40 45%,#b8962e 65%,#5a4a30)"></div>
  <p>owners in New Zealand regardless of Falcon kit type. Our intent for the Forum is to give those people interested/active in the RT Falcon NZ scene a common vehicle to share ideas</p>
  <span class="btn">Read more</span>
</article>

<section class="abs links" style="left:235px"><h3>Lorem Ipsum is</h3><ul><li>Lorem Ipsum is simply</li><li>Dummy text of the printing</li><li>Typesetting industry</li><li>Lorem Ipsum has been</li><li>Industry's standard</li><li>Dummy text of the printing</li><li>Typesetting industry</li><li>Lorem Ipsum has been</li></ul></section>
<section class="abs links" style="left:374px"><h3>Lorem Ipsum is</h3><ul><li>Lorem Ipsum is simply</li><li>Dummy text of the printing</li><li>Typesetting industry</li><li>Lorem Ipsum has been</li><li>Industry's standard</li><li>Dummy text of the printing</li><li>Typesetting industry</li><li>Lorem Ipsum has been</li></ul></section>
<section class="abs links" style="left:512px"><h3>Lorem Ipsum is</h3><ul><li>Lorem Ipsum is simply</li><li>Dummy text of the printing</li><li>Typesetting industry</li><li>Lorem Ipsum has been</li><li>Industry's standard</li><li>Dummy text of the printing</li><li>Typesetting industry</li><li>Lorem Ipsum has been</li></ul></section>
<section class="abs links" style="left:651px"><h3>Lorem Ipsum is</h3><ul><li>Lorem Ipsum is simply</li><li>Dummy text of the printing</li><li>Typesetting industry</li><li>Lorem Ipsum has been</li><li>Industry's standard</li><li>Dummy text of the printing</li><li>Typesetting industry</li><li>Lorem Ipsum has been</li></ul></section>

<aside class="abs sidebar" style="top:149px">
  <div class="box-head">Latest Events of Falcon Club</div>
  <ul class="events">
    <li><b>10</b>Lorem Ipsum is simply dummy</li>
    <li><b>10</b>text of the printing and typesetting</li>
    <li><b>12</b>Lorem Ipsum has been the indust</li>
    <li><b>12</b>Standard dummy text ever since</li>
    <li><b>12</b>When an unknown printer took</li>
    <li><b>13</b>Galley of type and scrambled it</li>
  </ul>
</aside>

<aside class="abs sidebar" style="top:349px">
  <div class="box-head">Forum Updates</div>
  <div class="panel forum">
    <div class="topic"><h4>Announcements</h4><p>Read this forum first to find out the latest information.</p><div class="stats"><span>Topics 20</span><span>Posts 60</span><span>Date 02/01/12</span></div></div>
    <div class="topic"><h4>Announcements</h4><p>Read this forum first to find out the latest information.</p><div class="stats"><span>Topics 20</span><span>Posts 60</span><span>Date 02/01/12</span></div></div>
    <div class="topic"><h4>Announcements</h4><p>Read this forum first to find out the latest information.</p><div class="stats"><span>Topics 20</span><span>Posts 60</span><span>Date 02/01/12</span></div></div>
    <div class="topic"><h4>Announcements</h4><p>Read this forum first to find out the latest information.</p><div class="stats"><span>Topics 20</span><span>Posts 60</span><span>Date 02/01/12</span></div></div>
    <div class="topic"><h4>Announcements</h4><p>Read this forum first to find out the latest information.</p><div class="stats"><span>Topics 20</span><span>Posts 60</span><span>Date 02/01/12</span></div></div>
  </div>
</aside>

<aside class="abs sidebar" style="top:768px">
  <div class="box-head">Social Circle</div>
  <div class="panel social">
    <span role="img" aria-label="Feed link" style="background:#f5b52a"></span>
    <span role="img" aria-label="Social network link" style="background:#3a5597"></span>
    <span role="img" aria-label="Social network link" style="background:#3fa6e0"></span>
    <span role="img" aria-label="Social network link" style="background:#68b3cf"></span>
  </div>
</aside>

<aside class="abs sidebar" style="top:858px">
  <div class="box-head">Sign up for Newsletter</div>
  <div class="panel newsletter">
    <div class="field">email address</div>
    <span class="btn">Subscribe</span>
  </div>
</aside>

<footer class="abs footer">Copyright © 2012 RT FALCON CLUB. Use of this website constitutes acceptance of our User Agreement</footer>
<div class="abs sponsored">This site is proudly Sponsored by<span class="sponsor-name">Kiwi Garage DIY</span></div>
</body>
</html>
```